Road Construction Company needs business cards

We would like a new business card designed for our business.

We're a road construction company based in Qld, Australia.

Can the business card please have the following information on it.

Name: Brent Malvoy
Position: General Manager
Phone: 0471 592 304
Email: Brent.malvoy@quendix.com.au
Address: 87 Harrowgate Ave, Pindarra, QLD, 4000
Website: www.quendix.com.au

Visually we'd like the card to be professional and simple.

Attached is our logo.

Our website is www.quendix.com.au

Target Market(s)

Men aged 25-60

Contact Information for Business Card

As listed in project description

Font styles to use
Serif

Requirements
Must have
• Large logo on back of card

```html
<!DOCTYPE html>
<html lang="en">
<head>
<meta charset="utf-8">
<title>Quendix Road Construction – Business Card</title>
<link href="https://fonts.googleapis.com/css2?family=Montserrat:wght@400;500;700;800&display=swap" rel="stylesheet">
<style>
  :root {
    --navy: #0e56a5;
    --sky: #31a3d8;
    --ink: #1d1d1f;
    --paper: #ffffff;
    --stage: #e4e6ea;
  }
  * { margin: 0; padding: 0; box-sizing: border-box; }
  html, body {
    width: 1200px; height: 1059px; overflow: hidden;
    background: var(--stage);
    font-family: "Montserrat", sans-serif;
  }
  .card {
    position: absolute;
    left: 256px;
    width: 688px;
    height: 391px;
    border-radius: 18px;
    overflow: hidden;
  }
  .card--front { top: 100px; background: var(--paper); }
  .card--back { top: 558px; background: var(--navy); }

  .brand-name {
    position: absolute; left: 0; right: 0;
    text-align: center;
    font-weight: 800;
    font-size: 62px;
    letter-spacing: 2px;
    line-height: 1;
    text-transform: uppercase;
  }
  .card--front .brand-name { top: 74px; color: var(--navy); }
  .card--back .brand-name { top: 162px; color: var(--paper); }

  .person-name {
    position: absolute; left: 0; right: 0; top: 208px;
    text-align: center;
    font-weight: 700; font-size: 28px;
    color: var(--navy);
  }
  .person-name .surname { color: var(--sky); }

  .role-rule {
    position: absolute; left: 30px; right: 30px; top: 241px;
    display: flex; align-items: center; gap: 8px;
  }
  .role-rule::before, .role-rule::after {
    content: ""; flex: 1; height: 1px; background: var(--sky);
  }
  .role-title { font-size: 17px; font-weight: 500; color: var(--ink); }

  .contact-list {
    position: absolute; left: 30px; top: 278px;
    list-style: none;
  }
  .contact-list li {
    display: flex; align-items: center; gap: 8px;
    height: 26px;
    font-size: 16.5px; color: var(--ink);
  }
  .contact-list svg { width: 13px; height: 13px; fill: var(--navy); flex: none; }

  .address {
    position: absolute; right: 31px; top: 311px;
    text-align: right;
    font-size: 16.5px; line-height: 20px; color: var(--ink);
  }

  .footer-band { position: absolute; left: 0; bottom: 0; width: 688px; height: 16px; }
</style>
</head>
<body>
  <section class="card card--front">
    <div class="brand-name">Quendix</div>
    <div class="person-name">Brent <span class="surname">Malvoy</span></div>
    <div class="role-rule"><span class="role-title">General Manager</span></div>

    <ul class="contact-list">
      <li>
        <svg viewBox="0 0 16 16" aria-hidden="true"><path d="M3.6 1.2l2.2 2.9-1.4 1.6c.9 2 2.6 3.8 4.7 4.8l1.6-1.5 2.9 2.2-1.3 2.7C6.9 13.6 2.3 9 1 3z"/></svg>
        0471 592 304
      </li>
      <li>
        <svg viewBox="0 0 16 16" aria-hidden="true"><path d="M1 3h14v1.2L8 8.8 1 4.2z M1 6l7 4.6L15 6v7H1z"/></svg>
        Brent.malvoy@quendix.com.au
      </li>
      <li>
        <svg viewBox="0 0 16 16" aria-hidden="true"><path d="M8 1a7 7 0 1 0 0 14A7 7 0 0 0 8 1zm0 1.3c.8 0 1.7 1.6 2 3.9H6c.3-2.3 1.2-3.9 2-3.9zM2.4 7.2h2.5c0 .6 0 1.1.1 1.6H2.4a5.7 5.7 0 0 1 0-1.6zm3.6 0h4c.1.5.1 1.1 0 1.6H6a8 8 0 0 1 0-1.6zm5.1 0h2.5a5.7 5.7 0 0 1 0 1.6h-2.5c.1-.5.1-1 0-1.6zM6 9.8h4c-.3 2.3-1.2 3.9-2 3.9s-1.7-1.6-2-3.9z"/></svg>
        www.quendix.com.au
      </li>
    </ul>

    <address class="address" style="font-style:normal">87 Harrowgate Ave,<br>Pindarra, QLD, 4000</address>

    <svg class="footer-band" viewBox="0 0 688 16" preserveAspectRatio="none" aria-hidden="true">
      <polygon points="0,0 352,0 334,16 0,16" fill="var(--navy)"/>
      <polygon points="360,0 688,0 688,16 342,16" fill="var(--sky)"/>
    </svg>
  </section>

  <section class="card card--back">
    <div class="brand-name">Quendix</div>
  </section>
</body>
</html>
```